International publishing business needs a book cover design

This will be the second book cover design I've had done through pixelharbor. You should be able to easily find my first one. The title of this new book is PEBBLES OF FOLLY: Unlikely True Tales from a Monastery Dropout. Yes, it's a comedy book. I picture the front cover having a laughing buddha with a smiling poop emoji somewhere near him, perhaps at his feet.
Updates

In case, it's unclear, the design should be FUNNY! 😊

Target Market(s)

Men 50 and up who love humor and are also "seekers" of wisdom and meaning in life.

Industry/Entity Type

humor books

Font styles to use
Other font styles liked:
• See the attached example. This font is pretty common for Buddhist books - kind of elegant and classy.

Colors
FFC000
F8CF3A
FAE287
FDF2CF
FEFAEE

Requirements
Must have
• An image of a laughing Buddha and a poop emoji, though the poop emoji does not need to be laughing or even smiling. It could be surprised.
Nice to have
• a classy look, that contradicts the absurd humor. Elegant. The color gold.
Should not have
• cartoons

```html
<!DOCTYPE html>
<html lang="en">
<head>
<meta charset="utf-8">
<title>Pebbles of Folly – Book Cover</title>
<link rel="stylesheet" href="https://fonts.googleapis.com/css2?family=Sniglet:wght@400;800&family=Patrick+Hand&display=swap">
<style>
  :root {
    --sky-top: #a8dcd6;
    --sky-mid: #cbe8e8;
    --city-haze: #bcdde4;
    --foliage-light: #6fbf6a;
    --foliage-dark: #2f8a45;
    --path-tan: #c9a66b;
    --road: #4a4a4c;
    --road-dark: #3c3c3e;
    --title-gold: #f5b335;
    --ink: #2a1f14;
    --white: #ffffff;
    --robe-orange: #ee6a24;
    --scooter-teal: #6fbcc0;
    --pebble-brown: #9a5a1e;
  }
  html, body {
    margin: 0;
    padding: 0;
    overflow: hidden;
    background: #ffffff;
  }
  .cover {
    position: relative;
    width: 800px;
    height: 1200px;
    overflow: hidden;
    font-family: "Sniglet", "Arial Rounded MT Bold", sans-serif;
  }
  .scene {
    position: absolute;
    inset: 0;
    background:
      linear-gradient(180deg,
        var(--sky-top) 0%,
        var(--sky-mid) 30%,
        var(--city-haze) 55%,
        var(--foliage-light) 64%,
        var(--foliage-dark) 70%,
        var(--path-tan) 74%,
        var(--foliage-light) 79%,
        var(--road) 84%,
        var(--road-dark) 100%);
  }
  .road-line {
    position: absolute;
    left: 0;
    width: 800px;
    top: 1058px;
    height: 4px;
    background: var(--white);
    opacity: 0.9;
  }
  .character {
    position: absolute;
    left: 180px;
    top: 520px;
    width: 440px;
    height: 520px;
    border-radius: 46% 46% 24% 24%;
    background: radial-gradient(ellipse at 50% 55%, var(--robe-orange) 0%, rgba(238,106,36,0.55) 40%, rgba(111,188,192,0.6) 70%, rgba(111,188,192,0) 100%);
  }
  .pebble {
    position: absolute;
    left: 48px;
    top: 990px;
    width: 70px;
    height: 58px;
    border-radius: 50% 50% 40% 40%;
    background: radial-gradient(circle at 45% 40%, #c07a30, var(--pebble-brown));
  }
  .title {
    position: absolute;
    left: 0;
    right: 0;
    top: 30px;
    margin: 0;
    text-align: center;
    color: var(--title-gold);
    font-weight: 800;
    line-height: 1;
    -webkit-text-stroke: 5px var(--ink);
    paint-order: stroke fill;
  }
  .title__main {
    display: block;
    font-size: 150px;
    letter-spacing: 2px;
  }
  .title__of {
    display: flex;
    align-items: center;
    justify-content: center;
    gap: 14px;
    font-size: 56px;
    margin: -4px 0 -2px;
  }
  .title__rule {
    width: 160px;
    height: 5px;
    border-radius: 3px;
    background: var(--title-gold);
    box-shadow: 0 0 0 2px var(--ink);
  }
  .title__second {
    display: block;
    font-size: 166px;
    letter-spacing: 1px;
  }
  .subtitle {
    position: absolute;
    left: 0;
    right: 0;
    top: 420px;
    margin: 0;
    text-align: center;
    font-family: "Patrick Hand", "Comic Sans MS", cursive;
    font-size: 38px;
    line-height: 1.1;
    color: var(--title-gold);
    -webkit-text-stroke: 3px var(--ink);
    paint-order: stroke fill;
  }
  .author {
    position: absolute;
    left: 0;
    right: 0;
    top: 1092px;
    margin: 0;
    text-align: center;
    font-size: 66px;
    font-weight: 800;
    color: var(--white);
    -webkit-text-stroke: 6px #111111;
    paint-order: stroke fill;
  }
</style>
</head>
<body>
  <main class="cover">
    <div class="scene" role="img" aria-label="Illustrated background: pale teal sky with hazy city buildings, green bushes and a dirt path above a grey asphalt road"></div>
    <div class="road-line"></div>
    <div class="character" role="img" aria-label="Cartoon laughing monk in an orange robe, cap and sunglasses riding a teal scooter"></div>
    <div class="pebble" role="img" aria-label="Small brown poop emoji sitting on the road"></div>

    <h1 class="title">
      <span class="title__main">PEBBLES</span>
      <span class="title__of"><span class="title__rule"></span>of<span class="title__rule"></span></span>
      <span class="title__second">FOLLY</span>
    </h1>
    <p class="subtitle">Unlikely True Tales<br>from a Monastery Dropout</p>

    <p class="author">Author Name</p>
  </main>
</body>
</html>
```